Offer banner redesign / Simplifying existing banner

We have a banner there customer can click on to get an offer. We want to simplify this banner and to get it to at minimum. We are not clear about how it shoulderstand look like, but the actual banner you can see here (It's at the top of the page): https://kaminwerk-bauvert.de/rauchrohr-system/ We want to get rid of the icons and to reduce the size of the baner. The baner shoulderstand contain the Following text: Affordable chimney using installation service button text: Request free quote

Target Market(s)

Customers from age of 40yrs.

Requirements
Must have
• Clear and good visible button
Nice to have
• It Should be simple and striking.

```html
<!DOCTYPE html>
<html lang="de">
<head>
<meta charset="utf-8">
<title>Kaminwerk Bauvert – Edelstahlschornstein</title>
<link rel="stylesheet" href="https://fonts.googleapis.com/css2?family=Fira+Sans:wght@400;500;600;700&family=Open+Sans:wght@400;600;700&display=swap">
<style>
:root{
  --orange:#f7b233;
  --orange-text:#ee9a10;
  --orange-soft:#f2b07a;
  --ink:#333333;
  --muted:#777777;
  --bar:#e6e4e4;
  --banner-bg:#f2f2f2;
  --line:#e2e2e2;
  --green:#23b528;
  --white:#ffffff;
  --star:#f2c200;
}
*{box-sizing:border-box;margin:0;padding:0}
html,body{width:1200px;height:675px;overflow:hidden;background:var(--white)}
body{position:relative;font-family:"Open Sans",Arial,sans-serif;color:var(--ink)}
.page{position:absolute;left:0;top:68px;width:1186px;height:492px;overflow:hidden;background:var(--white)}
.scrollbar{position:absolute;left:1186px;top:68px;width:14px;height:492px;background:#f1f1f1}
.scrollbar .thumb{position:absolute;left:3px;top:14px;width:8px;height:80px;background:#c1c1c1}

/* utility bar */
.util-bar{position:absolute;left:0;top:0;width:100%;height:29px;background:var(--bar);font-size:9px;letter-spacing:1px;color:#555}
.util-links{position:absolute;left:100px;top:0;height:29px;display:flex;align-items:center}
.util-links span{padding:0 12px;border-right:1px solid #999;line-height:16px}
.util-links span:first-child{padding-left:0}
.util-links span:last-child{border-right:none}
.caret{display:inline-block;margin-left:5px;border-left:4px solid transparent;border-right:4px solid transparent;border-top:4px solid #555;vertical-align:middle}
.util-rating{position:absolute;left:774px;top:8px;font-size:9px;font-weight:700;color:#333;letter-spacing:0}
.util-rating b{color:var(--star);font-size:12px;letter-spacing:-1px;margin-right:4px}
.util-btn{position:absolute;top:2px;height:27px;background:#d8d6d6;font-size:9px;letter-spacing:0;color:#444;display:flex;align-items:center;padding:0 8px;gap:6px}
.util-btn.account{left:913px;width:87px}
.util-btn.cart{left:1012px;width:81px}

/* header */
.header{position:absolute;left:0;top:29px;width:100%;height:58px;border-bottom:1px solid var(--line)}
.brand{position:absolute;left:95px;top:12px;display:flex;align-items:center;gap:8px}
.brand-dot{width:36px;height:36px;border-radius:50%;background:var(--orange)}
.brand-name{font-family:"Fira Sans",sans-serif;font-weight:600;font-size:17px;line-height:18px;color:#3a3a3a;letter-spacing:.3px}
.search{position:absolute;left:436px;top:10px;width:314px;height:35px;border:2px solid #d9d9d9;border-radius:10px;overflow:hidden;background:var(--white)}
.search span{position:absolute;left:0;width:276px;top:8px;text-align:center;font-size:12px;color:#b5b5b5}
.search .go{position:absolute;right:0;top:0;width:37px;height:31px;background:var(--orange)}
.hotline{position:absolute;right:92px;top:12px;text-align:right}
.hotline .number{font-family:"Fira Sans",sans-serif;font-weight:600;font-size:17px;color:var(--orange);display:flex;align-items:center;gap:8px;justify-content:flex-end}
.hotline .hours{font-size:9.5px;color:#444;margin-top:4px}

/* navigation */
.nav{position:absolute;left:0;top:87px;width:100%;height:40px;border-bottom:1px solid var(--line)}
.nav-items{position:absolute;left:108px;top:0;height:40px;display:flex;align-items:center;font-family:"Fira Sans",sans-serif;font-weight:500;font-size:14px;color:#333}
.nav-items span{display:flex;align-items:center;gap:10px;padding-right:16px}
.nav-items span+span{border-left:1px solid #ccc;padding-left:16px;line-height:14px}
.review{position:absolute;left:908px;top:5px;display:flex;align-items:center;gap:12px}
.review-badge{width:31px;height:31px;border-radius:50%;background:#2b2b2b}
.review-label{font-size:9px;color:#8aa5b5;text-align:center;line-height:14px}
.review-label b{display:block;color:var(--star);font-size:12px;letter-spacing:-1px}
.review-score{text-align:center;font-size:9px;font-weight:700;color:#333;line-height:14px}
.review-score strong{display:block;font-size:13px}
.review-score strong small{font-weight:400;font-size:13px;color:#555}

/* offer banner – compact, no icons */
.offer-banner{position:absolute;left:0;top:127px;width:100%;height:110px;background:var(--banner-bg)}
.offer-banner svg{position:absolute;left:0;top:0}
.offer-copy{position:absolute;left:300px;width:480px;top:24px;text-align:center;font-family:"Fira Sans",sans-serif;color:var(--orange-text)}
.offer-copy h2{font-weight:700;font-size:24px;letter-spacing:.8px;line-height:28px}
.offer-copy p{font-weight:400;font-size:19px;letter-spacing:.6px;line-height:24px;margin-top:4px}
.offer-cta{position:absolute;left:826px;top:33px;width:268px;height:44px;background:var(--orange);border-radius:4px;display:flex;align-items:center;justify-content:center;font-family:"Fira Sans",sans-serif;font-weight:700;font-size:13px;letter-spacing:1px;color:#2b2b2b}

/* category */
.breadcrumb{position:absolute;left:92px;top:243px;font-family:"Fira Sans",sans-serif;font-size:11px;color:var(--orange-soft)}
.breadcrumb i{font-style:normal;color:#999;margin:0 12px}
.category-title{position:absolute;left:350px;top:276px;font-family:"Fira Sans",sans-serif;font-weight:500;font-size:22px;color:#333}
.pager{position:absolute;left:358px;top:314px;display:flex;gap:10px;font-size:11px;color:#999}
.pager span{width:20px;height:20px;display:flex;align-items:center;justify-content:center;border-radius:50%}
.pager .current{background:#a3a3a3;color:var(--white)}
.pager .soft{color:#d49a6a}
.per-page{position:absolute;left:987px;top:312px;display:flex;align-items:center;gap:12px;font-family:"Fira Sans",sans-serif;font-size:13px;color:#999;font-weight:500}
.per-page span{width:56px;height:26px;background:#a8a8a8;color:var(--white);display:flex;align-items:center;justify-content:space-between;padding:0 8px;font-weight:400}
.list-rule{position:absolute;left:350px;top:346px;width:744px;height:1px;background:var(--line)}
.filter{position:absolute;left:92px;top:354px;width:230px;height:41px;background:var(--orange);color:var(--white);font-size:13px;display:flex;align-items:center;justify-content:space-between;padding:0 12px}
.product-card{position:absolute;top:370px;width:358px;height:122px;border:2px solid #eee;border-bottom:none;text-align:center;font-family:"Fira Sans",sans-serif;font-weight:500;font-size:13px;line-height:21px;color:#333;padding-top:12px}
.product-card.first{left:349px}
.product-card.second{left:735px}
.live-chat{position:absolute;left:18px;top:452px;width:125px;height:40px;background:var(--green);border-radius:4px 4px 0 0;color:var(--white);font-family:"Fira Sans",sans-serif;font-weight:700;font-size:12px;display:flex;align-items:center;gap:10px;padding-left:17px}
</style>
</head>
<body>
<main class="page">
  <div class="util-bar">
    <div class="util-links">
      <span>SICHER EINKAUFEN<i class="caret"></i></span>
      <span>VORTEILE<i class="caret"></i></span>
      <span>BERATUNG &amp; KONTAKT<i class="caret"></i></span>
    </div>
    <div class="util-rating"><b>★★★★★</b>(4.55/5.00) ✓</div>
    <div class="util-btn account">Mein Konto
      <svg width="16" height="16" viewBox="0 0 16 16"><circle cx="8" cy="5" r="4" fill="#333"/><path d="M1 16c0-5 3-7 7-7s7 2 7 7z" fill="#333"/></svg>
    </div>
    <div class="util-btn cart">Warenkorb
      <svg width="20" height="18" viewBox="0 0 20 18"><circle cx="14" cy="4" r="4" fill="#f7b233"/><path d="M2 8h16l-2 9H4z" fill="#333"/></svg>
    </div>
  </div>

  <header class="header">
    <div class="brand">
      <div class="brand-dot"></div>
      <div class="brand-name">KAMINWERK<br>BAUVERT</div>
    </div>
    <div class="search"><span>Suchbegriff oder Artikelnummer:</span>
      <div class="go"><svg width="37" height="31" viewBox="0 0 37 31"><circle cx="17" cy="14" r="5" fill="none" stroke="#fff" stroke-width="2.5"/><path d="M21 18l4 4" stroke="#fff" stroke-width="2.5"/></svg></div>
    </div>
    <div class="hotline">
      <div class="number"><svg width="18" height="18" viewBox="0 0 18 18"><path d="M4 1l3 4-2 2c1 2 3 4 5 5l2-2 4 3-2 3C8 16 2 10 1 4z" fill="#f7b233"/></svg>04321 / 778 120 5</div>
      <div class="hours">Mo. - Fr. von 09:00 bis 18:00 Uhr</div>
    </div>
  </header>

  <nav class="nav">
    <div class="nav-items">
      <span>Online-Shop <svg width="10" height="6" viewBox="0 0 10 6"><path d="M1 1l4 4 4-4" fill="none" stroke="#f7b233"/></svg></span>
      <span>Service <svg width="10" height="6" viewBox="0 0 10 6"><path d="M1 1l4 4 4-4" fill="none" stroke="#f7b233"/></svg></span>
    </div>
    <div class="review">
      <div class="review-badge"></div>
      <div class="review-label">Kundenbewertung<b>★★★★★</b></div>
      <div class="review-score">sehr gut<strong>4.55<small>/5.00</small></strong></div>
    </div>
  </nav>

  <section class="offer-banner">
    <svg width="300" height="110" viewBox="0 0 300 110">
      <defs>
        <linearGradient id="sceneTone" x1="0" y1="0" x2="0" y2="1">
          <stop offset="0" stop-color="#9fc3dc"/>
          <stop offset="0.6" stop-color="#b8bec2"/>
          <stop offset="1" stop-color="#4f6a3a"/>
        </linearGradient>
      </defs>
      <polygon points="0,0 270,0 207,110 0,110" fill="url(#sceneTone)" role="img" aria-label="Foto: modernes Flachdachhaus mit Edelstahlschornstein"/>
      <polygon points="252,0 270,0 207,110 189,110" fill="#f7b233"/>
    </svg>
    <div class="offer-copy">
      <h2>PREISWERTER SCHORNSTEIN</h2>
      <p>WAHLWEISE MIT MONTAGESERVICE</p>
    </div>
    <div class="offer-cta">KOSTENLOSES ANGEBOT ANFORDERN</div>
  </section>

  <div class="breadcrumb">Kaminwerk-Bauvert<i>&gt;</i>Edelstahlschornstein</div>
  <h1 class="category-title">Edelstahlschornstein</h1>
  <div class="pager"><span class="current">1</span><span>2</span><span>3</span><span class="soft">4</span><span>5</span></div>
  <div class="per-page">Zeige <span>12 <svg width="10" height="6" viewBox="0 0 10 6"><path d="M1 1l4 4 4-4" fill="none" stroke="#fff"/></svg></span></div>
  <div class="list-rule"></div>
  <div class="filter">Filter <svg width="11" height="11" viewBox="0 0 11 11"><path d="M0 0h11L7 5v6L4 9V5z" fill="#fff"/></svg></div>

  <article class="product-card first">Edelstahlschornstein doppelwandig Ø 150 mm<br>Bausatz - Tervald DW-ECO</article>
  <article class="product-card second">Edelstahlschornstein doppelwandig Ø 150 mm<br>Bausatz - Tervald DW-EU</article>

  <div class="live-chat">
    <svg width="26" height="22" viewBox="0 0 26 22"><path d="M2 1h22v14H10l-6 6v-6H2z" fill="#fff"/><circle cx="8" cy="8" r="1.6" fill="#23b528"/><circle cx="13" cy="8" r="1.6" fill="#23b528"/><circle cx="18" cy="8" r="1.6" fill="#23b528"/></svg>
    Live-Chat
  </div>
</main>
<div class="scrollbar"><div class="thumb"></div></div>
</body>
</html>
```